Tulven Electrics Flyer Design Advertising

I am after an A5 Flyer design to help promote my electrical services business.
I would like to have information on what my business offers, photos of electrical work, and specials/deals for an amount of time.

Industry/Entity Type

Electrician

Font styles to use
Sans Serif

Colors
0292cd
33a6d7
85cae6
3176b5
333333
1b1b1b
ffffff
5c5c5c
474747

Requirements
Must have
• Specialising in New homes, renovations and commercial projects
• Contact details:
• ph. 0437 619 458
• email admin@tulvenelectrics.example.au
• facebook TulvenElectrics
• Specials/Deals:
• 10% off all electrical services
• or
• Free LED downlights on installation
• *Terms conditions apply
• ALL RESIDENTIAL & COMMERCIAL ELECTRICAL SERVICES
• - New Home installations
• - Commercial projects
• - Shop fit outs
• - Renovations
• - Smoke Detectors
• - Air Conditioning and Ceiling Fans
• - Garden Lighting
• - Oven and Cooktop Installations
• - Power Point installation
• - LED lighting upgrades
• - Security Lighting
• - Switchboard upgrades
• - Test and Tag
• - Commercial Property
• - General Electrical Maintenance

```html
<!DOCTYPE html>
<html lang="en">
<head>
<meta charset="utf-8">
<title>Tulven Electrics Flyer</title>
<link rel="stylesheet" href="https://fonts.googleapis.com/css2?family=Montserrat:wght@400;500;700&family=Arimo:wght@400;700&display=swap">
<style>
  :root {
    --blue: #0292cd;
    --blue-soft: #33a6d7;
    --blue-pale: #85cae6;
    --blue-deep: #3176b5;
    --charcoal: #333333;
    --ink: #1b1b1b;
    --white: #ffffff;
    --grey: #5c5c5c;
    --grey-dark: #474747;
    --page: #e6e6e6;
  }
  html, body {
    margin: 0;
    padding: 0;
    width: 1200px;
    height: 1100px;
    overflow: hidden;
    background: var(--page);
  }
  .canvas {
    position: relative;
    width: 1200px;
    height: 1100px;
  }
  .flyer {
    position: absolute;
    left: 233px;
    top: 29px;
    width: 734px;
    height: 1041px;
    display: block;
  }
  .heading { font-family: "Montserrat", sans-serif; font-size: 24px; }
  .heading .strong { font-weight: 700; }
  .heading .slash { font-weight: 700; font-style: italic; }
  .heading-dark { fill: var(--ink); }
  .heading-light { fill: var(--white); }
  .deal-title { font-family: "Montserrat", sans-serif; font-size: 15px; fill: var(--ink); }
  .deal-text { font-family: "Montserrat", sans-serif; font-size: 7.6px; font-weight: 500; fill: var(--ink); }
  .deal-terms { font-family: "Montserrat", sans-serif; font-size: 8px; fill: var(--ink); }
  .offer-item { font-family: "Arimo", sans-serif; font-size: 14.5px; fill: var(--ink); }
  .tick-ring { fill: none; stroke: var(--white); stroke-width: 1.3; }
  .tick-mark { fill: none; stroke: var(--white); stroke-width: 1.4; stroke-linecap: round; stroke-linejoin: round; }
  .contact-text { font-family: "Montserrat", sans-serif; font-size: 16px; fill: var(--ink); }
  .contact-email { font-size: 12.2px; font-weight: 500; }
  .contact-icon { fill: none; stroke: var(--white); stroke-width: 1.5; stroke-linejoin: round; stroke-linecap: round; }
  .brand-name { font-family: "Montserrat", sans-serif; font-size: 19px; font-weight: 700; fill: var(--white); }
  .tile-caption { font-family: "Arimo", sans-serif; font-size: 10.5px; fill: var(--white); }
</style>
</head>
<body>
<div class="canvas">
  <svg class="flyer" viewBox="0 0 600 851" xmlns="http://www.w3.org/2000/svg" aria-label="Tulven Electrics service flyer">
    <defs>
      <linearGradient id="hero-tone" x1="0" y1="0" x2="0.6" y2="1">
        <stop offset="0" stop-color="#3f6c8e"/>
        <stop offset="0.35" stop-color="#7d96a8"/>
        <stop offset="0.65" stop-color="#3c5a4c"/>
        <stop offset="1" stop-color="#1f4a5a"/>
      </linearGradient>
      <linearGradient id="kitchen-tone" x1="0" y1="0" x2="0" y2="1">
        <stop offset="0" stop-color="#d9dcdf"/>
        <stop offset="1" stop-color="#4a4d52"/>
      </linearGradient>
      <linearGradient id="cottage-tone" x1="0" y1="0" x2="0" y2="1">
        <stop offset="0" stop-color="#6f8fb5"/>
        <stop offset="0.6" stop-color="#b79a6a"/>
        <stop offset="1" stop-color="#2f3a2a"/>
      </linearGradient>
      <linearGradient id="garden-tone" x1="0" y1="0" x2="0" y2="1">
        <stop offset="0" stop-color="#2a4f8c"/>
        <stop offset="0.6" stop-color="#6a5a44"/>
        <stop offset="1" stop-color="#1d2a22"/>
      </linearGradient>
    </defs>

    <!-- hero photo area -->
    <rect class="hero-photo" x="0" y="0" width="600" height="600" fill="url(#hero-tone)" role="img" aria-label="Modern two-storey home with warm lit windows at dusk, surrounded by garden"/>

    <!-- specials box -->
    <rect class="specials-box" x="452" y="53" width="148" height="157" fill="var(--blue-soft)" fill-opacity="0.85"/>
    <text class="deal-title" x="464" y="79"><tspan class="slash" font-weight="700" font-style="italic">//</tspan> Specials <tspan font-weight="700">Deals</tspan></text>
    <text class="deal-text" x="461" y="112">10% off all electrical services</text>
    <text class="deal-text" x="461" y="124">Or Free LED downlights</text>
    <text class="deal-text" x="461" y="135">on installation</text>
    <text class="deal-terms" x="589" y="166" text-anchor="end">Terms conditions apply</text>

    <!-- offer band -->
    <polygon class="offer-band" points="0,318 600,222 600,437 0,562" fill="var(--blue)" fill-opacity="0.8"/>
    <line class="offer-divider" x1="300" y1="300" x2="300" y2="480" stroke="var(--blue-pale)" stroke-width="1" stroke-dasharray="3 3"/>

    <text class="heading heading-dark" x="585" y="276" text-anchor="end"><tspan class="slash">//</tspan> What <tspan class="strong">We Offer</tspan></text>

    <g class="offer-list offer-list-right">
      <g transform="translate(333,300)"><circle class="tick-ring" r="7"/><path class="tick-mark" d="M-3,0 L-0.8,2.5 L3.2,-2.5"/></g>
      <text class="offer-item" x="353" y="305">New Home installations</text>
      <g transform="translate(333,321)"><circle class="tick-ring" r="7"/><path class="tick-mark" d="M-3,0 L-0.8,2.5 L3.2,-2.5"/></g>
      <text class="offer-item" x="353" y="326">Commercial projects</text>
      <g transform="translate(333,342)"><circle class="tick-ring" r="7"/><path class="tick-mark" d="M-3,0 L-0.8,2.5 L3.2,-2.5"/></g>
      <text class="offer-item" x="353" y="347">Shop fit outs</text>
      <g transform="translate(333,363)"><circle class="tick-ring" r="7"/><path class="tick-mark" d="M-3,0 L-0.8,2.5 L3.2,-2.5"/></g>
      <text class="offer-item" x="353" y="368">Renovations</text>
      <g transform="translate(333,385)"><circle class="tick-ring" r="7"/><path class="tick-mark" d="M-3,0 L-0.8,2.5 L3.2,-2.5"/></g>
      <text class="offer-item" x="353" y="390">Smoke Detectors</text>
      <g transform="translate(333,406)"><circle class="tick-ring" r="7"/><path class="tick-mark" d="M-3,0 L-0.8,2.5 L3.2,-2.5"/></g>
      <text class="offer-item" x="353" y="411">Air Conditioning and Ceiling Fans</text>
      <g transform="translate(333,427)"><circle class="tick-ring" r="7"/><path class="tick-mark" d="M-3,0 L-0.8,2.5 L3.2,-2.5"/></g>
      <text class="offer-item" x="353" y="432">Garden Lighting</text>
    </g>

    <g class="offer-list offer-list-left">
      <g transform="translate(30,337)"><circle class="tick-ring" r="7"/><path class="tick-mark" d="M-3,0 L-0.8,2.5 L3.2,-2.5"/></g>
      <text class="offer-item" x="49" y="342">Oven and Cooktop Installations</text>
      <g transform="translate(30,358)"><circle class="tick-ring" r="7"/><path class="tick-mark" d="M-3,0 L-0.8,2.5 L3.2,-2.5"/></g>
      <text class="offer-item" x="49" y="363">Power Point installation</text>
      <g transform="translate(30,379)"><circle class="tick-ring" r="7"/><path class="tick-mark" d="M-3,0 L-0.8,2.5 L3.2,-2.5"/></g>
      <text class="offer-item" x="49" y="384">LED lighting upgrades</text>
      <g transform="translate(30,400)"><circle class="tick-ring" r="7"/><path class="tick-mark" d="M-3,0 L-0.8,2.5 L3.2,-2.5"/></g>
      <text class="offer-item" x="49" y="405">Security Lighting</text>
      <g transform="translate(30,422)"><circle class="tick-ring" r="7"/><path class="tick-mark" d="M-3,0 L-0.8,2.5 L3.2,-2.5"/></g>
      <text class="offer-item" x="49" y="427">Switchboard upgrades</text>
      <g transform="translate(30,443)"><circle class="tick-ring" r="7"/><path class="tick-mark" d="M-3,0 L-0.8,2.5 L3.2,-2.5"/></g>
      <text class="offer-item" x="49" y="448">Test and Tag</text>
      <g transform="translate(30,464)"><circle class="tick-ring" r="7"/><path class="tick-mark" d="M-3,0 L-0.8,2.5 L3.2,-2.5"/></g>
      <text class="offer-item" x="49" y="469">Commercial Property</text>
      <g transform="translate(30,485)"><circle class="tick-ring" r="7"/><path class="tick-mark" d="M-3,0 L-0.8,2.5 L3.2,-2.5"/></g>
      <text class="offer-item" x="49" y="490">General Electrical Maintenance</text>
    </g>

    <!-- services panel -->
    <polygon class="services-panel" points="0,562 600,437 600,851 0,851" fill="var(--ink)"/>
    <polygon class="contact-panel" points="0,581 292,520 292,851 0,851" fill="var(--blue)"/>

    <!-- brand -->
    <circle class="brand-dot" cx="277" cy="546" r="32" fill="var(--charcoal)" stroke="var(--ink)" stroke-width="4"/>
    <text class="brand-name" x="318" y="553">Tulven Electrics</text>

    <text class="heading heading-light" x="582" y="519" text-anchor="end"><tspan class="slash" fill="var(--blue)">//</tspan> Our <tspan class="strong">Services</tspan></text>

    <!-- contact -->
    <text class="heading heading-dark" x="20" y="638"><tspan class="slash" fill="var(--white)">//</tspan> Contact <tspan class="strong">Us</tspan></text>

    <path class="contact-icon" d="M24,677 c2,-2 4,-2 5,0 l2,3 c1,2 0,3 -1,4 c1,3 4,6 7,7 c1,-1 2,-2 4,-1 l3,2 c2,1 2,3 0,5 c-3,3 -8,2 -13,-3 c-5,-5 -7,-11 -7,-17 z"/>
    <path class="contact-icon" d="M37,676 a8,8 0 0 1 7,7 M37,671 a13,13 0 0 1 12,12"/>
    <text class="contact-text" x="57" y="690">0437 619 458</text>

    <rect class="contact-icon" x="22" y="722" width="22" height="14" rx="1.5"/>
    <path class="contact-icon" d="M22,732 H44 M30,741 H36 M33,736 V741"/>
    <text class="contact-text contact-email" x="57" y="735">admin@tulvenelectrics.example.au</text>

    <rect class="social-square" x="22" y="767" width="20" height="20" fill="var(--white)"/>
    <text class="contact-text" x="57" y="783">TulvenElectrics</text>

    <!-- service tiles -->
    <rect class="tile-photo" x="299" y="583" width="144" height="135" fill="url(#kitchen-tone)" role="img" aria-label="Bright modern kitchen with pendant lights and island bench"/>
    <rect class="tile-strip" x="299" y="694" width="144" height="18" fill="var(--ink)" fill-opacity="0.7"/>
    <text class="tile-caption" x="371" y="707" text-anchor="middle">Home Installations</text>

    <rect class="tile-photo" x="456" y="583" width="144" height="135" fill="url(#cottage-tone)" role="img" aria-label="Raised timber house with lit windows and front stairs at dusk"/>
    <rect class="tile-strip" x="456" y="694" width="144" height="18" fill="var(--ink)" fill-opacity="0.7"/>
    <text class="tile-caption" x="528" y="707" text-anchor="middle">Electrical Maintenance</text>

    <rect class="tile-photo" x="299" y="726" width="301" height="112" fill="url(#garden-tone)" role="img" aria-label="Modern home at night with palm trees and illuminated garden lighting"/>
    <rect class="tile-strip" x="299" y="820" width="301" height="18" fill="var(--ink)" fill-opacity="0.55"/>
    <text class="tile-caption" x="450" y="833" text-anchor="middle">Garden Lighting</text>
  </svg>
</div>
</body>
</html>
```